Business Card for Lorena Whitfield

Name: Lorena Whitfield
Title: Realtor
Email: Lorena@LorenaWhitfieldRE.com
Phone: 480-555-0137

On the front of the business card, I would like the photo, the contact information and the Lorena Whitfield Logo. The backside is required to have the Broker logo and the required logos. Please use the colors from the logo design. Our company has a classy, professional look.

```html
<!DOCTYPE html>
<html lang="en">
<head>
<meta charset="utf-8">
<title>Lorena Whitfield – Business Card</title>
<link rel="stylesheet" href="https://fonts.googleapis.com/css2?family=Libre+Baskerville:wght@400;700&display=swap">
<style>
  :root {
    --crimson: #b51a35;
    --charcoal: #4a4a4a;
    --paper: #f7f7f7;
    --ink: #2b2b2b;
    --stage: #e6e3de;
    --ring: #555555;
    --white: #ffffff;
  }
  * { box-sizing: border-box; margin: 0; padding: 0; }
  html, body {
    width: 900px; height: 1200px; overflow: hidden;
    background: var(--stage);
    font-family: "Libre Baskerville", Georgia, serif;
  }
  .card {
    position: absolute;
    border-radius: 22px;
    overflow: hidden;
    background: var(--paper);
    box-shadow: 0 6px 18px rgba(0,0,0,.18);
  }
  .card-front { left: 72px; top: 135px; width: 773px; height: 448px; }
  .card-back  { left: 75px; top: 618px; width: 770px; height: 462px; }
  .card-shapes { position: absolute; inset: 0; }

  .brand {
    position: absolute;
    display: flex; align-items: center; gap: 14px;
    color: var(--crimson);
    font-weight: 400;
    text-transform: uppercase;
  }
  .brand-mark { width: 20px; height: 20px; background: var(--crimson); flex: none; }
  .brand-name { line-height: 1.15; }
  .brand-name span { display: block; text-align: right; font-size: .52em; letter-spacing: .04em; }

  .front-brand { left: 46px; top: 74px; font-size: 30px; }

  .agent { position: absolute; left: 38px; top: 230px; color: var(--white); font-weight: 700; }
  .agent-name { font-size: 27px; letter-spacing: .02em; text-transform: uppercase; }
  .agent-title { font-size: 21px; margin-top: 4px; }
  .contact { list-style: none; margin-top: 30px; font-size: 20px; }
  .contact li { display: flex; align-items: center; gap: 12px; margin-bottom: 14px; }
  .contact svg { flex: none; }

  .portrait {
    position: absolute; left: 453px; top: 42px;
    width: 286px; height: 286px; border-radius: 50%;
    background: var(--white);
    border: 3px solid var(--ring);
    padding: 6px;
  }
  .portrait-fill {
    width: 100%; height: 100%; border-radius: 50%;
    background: radial-gradient(circle at 50% 40%, #9a9a9a 0%, #6e6e6e 55%, #3c3c3c 100%);
  }

  .back-brand { left: 58px; top: 88px; font-size: 33px; color: var(--white); }
  .back-brand .brand-mark { background: var(--white); width: 24px; height: 24px; }

  .badges { position: absolute; left: 52px; top: 300px; display: flex; align-items: flex-end; gap: 14px; }
  .broker {
    width: 132px; height: 120px;
    display: flex; flex-direction: column; align-items: center; justify-content: flex-end; gap: 8px;
    color: var(--ink); font-size: 12px; text-transform: uppercase; text-align: center; letter-spacing: .04em;
  }
  .broker-mark { width: 62px; height: 62px; border-radius: 50%; border: 2px solid var(--ink); }
  .badge-housing { width: 92px; height: 104px; background: var(--ink); }
  .badge-realtor { width: 74px; height: 94px; border: 3px solid var(--ink); }
  .badge-listing { width: 106px; height: 60px; border: 2px solid var(--ink); }
</style>
</head>
<body>

<section class="card card-front" aria-label="Card front">
  <svg class="card-shapes" width="773" height="448" viewBox="0 0 773 448" aria-hidden="true">
    <polygon points="0,193 563,193 498,448 0,448" fill="var(--charcoal)"/>
    <polygon points="623,0 773,0 773,448 508,448" fill="var(--crimson)"/>
  </svg>

  <div class="brand front-brand">
    <div class="brand-mark"></div>
    <div class="brand-name">Lorena Whitfield<span>Real Estate</span></div>
  </div>

  <div class="agent">
    <h1 class="agent-name">Lorena Whitfield</h1>
    <p class="agent-title">Realtor</p>
    <ul class="contact">
      <li>
        <svg width="26" height="20" viewBox="0 0 26 20" aria-hidden="true"><path d="M2 7 Q13 -1 24 7 L21 10 L17 7 L17 5 Q13 3 9 5 L9 7 L5 10 Z" fill="#fff"/><rect x="6" y="11" width="14" height="8" rx="2" fill="#fff"/><circle cx="13" cy="15" r="2.5" fill="var(--charcoal)"/></svg>
        480-555-0137
      </li>
      <li>
        <svg width="26" height="18" viewBox="0 0 26 18" aria-hidden="true"><rect x="1" y="1" width="24" height="16" fill="#fff"/><path d="M1 1 L13 10 L25 1" fill="none" stroke="var(--charcoal)" stroke-width="1.6"/></svg>
        Lorena@LorenaWhitfieldRE.com
      </li>
    </ul>
  </div>

  <div class="portrait">
    <div class="portrait-fill" role="img" aria-label="Portrait photo of Lorena Whitfield"></div>
  </div>
</section>

<section class="card card-back" aria-label="Card back">
  <svg class="card-shapes" width="770" height="462" viewBox="0 0 770 462" aria-hidden="true">
    <polygon points="0,0 625,0 558,262 0,262" fill="var(--charcoal)"/>
    <polygon points="635,0 770,0 770,462 515,462" fill="var(--crimson)"/>
  </svg>

  <div class="brand back-brand">
    <div class="brand-mark"></div>
    <div class="brand-name">Lorena Whitfield<span>Real Estate</span></div>
  </div>

  <div class="badges">
    <div class="broker">
      <div class="broker-mark"></div>
      <p>Marlow Crest<br>Realty</p>
    </div>
    <div class="badge-housing" role="img" aria-label="Fair housing badge"></div>
    <div class="badge-realtor" role="img" aria-label="Realtor association badge"></div>
    <div class="badge-listing" role="img" aria-label="Listing service badge"></div>
  </div>
</section>

</body>
</html>
```